Human Resource Consulting practice needs a business card design

We need a business card design (double sided colour) for our Human Resource (HR) consulting practice in regional New South Wales, australia. Our business name is Staffwise Partners. We support small and medium business across the Mid North Coast of New South Wales by providing them with outsourced HR support, services and products to help them achieve compliance with workplace legislation and across all areas of the employment lifecycle from recruitment to termination and everything in between. Our corporate colours are hot pink and black. The final design should communicate professionalism, trust, people focus.
I have attached the current (old) business card for your reference.

Target Market(s)

Business owners and high level managers

Industry/Entity Type

Business

Contact Information for Business Card

Name
Title
Phone no
Mobile no
Address
PO Box
email address
website

Colors
e34197

Requirements
Must have
• Tempate for changing business card personal details including Name, position title, mobile number, email address.
• Keep current logo and colours as per attached
• Logo must be presented in 2 colours or black only not white
Nice to have
• One side logo and graphic only other side logo and personal details
Should not have
• Should not be the same as the current version (attached) but a modern interpretation.
• Does not need a busy reverse side with our list of services as per current version. I feel this is too busy.
• No photos

```html
<!DOCTYPE html>
<html lang="en">
<head>
<meta charset="utf-8">
<title>Staffwise Partners — Business Card</title>
<link rel="stylesheet" href="https://fonts.googleapis.com/css2?family=Oswald:wght@500;600&family=Play:wght@400;700&display=swap">
<style>
  :root {
    --pink: #e62a91;
    --charcoal: #38383a;
    --white: #ffffff;
    --ink: #2b2b2d;
    --star: #b9b9bb;
    --page: #ecebe8;
    --card-w: 760px;
    --card-h: 434px;
  }
  * { box-sizing: border-box; margin: 0; padding: 0; }
  html, body { width: 1200px; height: 1018px; overflow: hidden; }
  body {
    background: var(--page);
    font-family: "Play", sans-serif;
    display: flex;
    flex-direction: column;
    align-items: center;
    justify-content: center;
    gap: 50px;
  }
  .card {
    position: relative;
    width: var(--card-w);
    height: var(--card-h);
    overflow: hidden;
    box-shadow: 0 10px 26px rgba(0,0,0,.18);
  }

  /* Front */
  .card--front { background: var(--pink); }
  .front__dark {
    position: absolute; left: 0; top: 0;
    width: 78%; height: 76%;
    background: var(--charcoal);
  }
  .front__white {
    position: absolute; left: 0; top: 0;
    width: 70%; height: 54%;
    background: var(--white);
    display: flex; align-items: center; justify-content: center;
  }
  .brand { display: flex; align-items: center; gap: 12px; }
  .brand__dot {
    width: 16px; height: 16px; border-radius: 50%;
    background: var(--pink);
  }
  .brand__name {
    font-family: "Play", sans-serif;
    font-weight: 700;
    font-size: 40px;
    color: var(--ink);
    letter-spacing: .5px;
  }
  .contacts {
    position: absolute; left: 34px; top: 59%;
    display: grid;
    grid-template-columns: auto auto;
    column-gap: 34px; row-gap: 12px;
    color: var(--white);
    font-size: 14px;
    letter-spacing: .6px;
  }
  .contact { display: flex; align-items: center; gap: 9px; }
  .contact svg { width: 14px; height: 14px; fill: none; stroke: var(--white); stroke-width: 1.6; }
  .person {
    position: absolute; left: 34px; bottom: 22px;
    color: var(--white);
  }
  .person__name {
    font-family: "Oswald", sans-serif;
    font-weight: 600; font-size: 28px;
    letter-spacing: 1px; line-height: 1.1;
    text-transform: uppercase;
  }
  .person__title {
    font-size: 14px; letter-spacing: 2px;
    text-transform: uppercase;
  }
  .address {
    position: absolute; right: 22px; top: 28px;
    width: 18%;
    color: var(--white);
    font-size: 14px; line-height: 1.5;
    letter-spacing: .6px;
    text-align: right;
  }

  /* Back */
  .card--back { background: var(--charcoal); }
  .card--back svg { position: absolute; inset: 0; width: 100%; height: 100%; }
</style>
</head>
<body>

<section class="card card--front" aria-label="Business card front">
  <div class="front__dark"></div>
  <div class="front__white">
    <div class="brand">
      <span class="brand__dot"></span>
      <span class="brand__name">Staffwise Partners</span>
    </div>
  </div>

  <div class="contacts">
    <div class="contact">
      <svg viewBox="0 0 16 16"><path d="M4 1.5l2.2 3-1.3 1.6a9 9 0 0 0 5 5l1.6-1.3 3 2.2-1.2 2.3C8 14 2 8 1.7 2.7z"/></svg>
      <span>026 555 0148</span>
    </div>
    <div class="contact">
      <svg viewBox="0 0 16 16"><rect x="2" y="3.5" width="12" height="9" rx="1"/><path d="M2 4l6 5 6-5"/></svg>
      <span>dreeve@staffwise.net</span>
    </div>
    <div class="contact">
      <svg viewBox="0 0 16 16"><rect x="4" y="1.5" width="8" height="13" rx="1.5"/><path d="M7 12h2"/></svg>
      <span>026 555 0148</span>
    </div>
    <div class="contact">
      <svg viewBox="0 0 16 16"><circle cx="8" cy="8" r="6.3"/><path d="M1.7 8h12.6M8 1.7c-3 3.4-3 9.2 0 12.6M8 1.7c3 3.4 3 9.2 0 12.6"/></svg>
      <span>www.staffwisepartners.net</span>
    </div>
  </div>

  <div class="person">
    <p class="person__name">Daniel Reeve</p>
    <p class="person__title">General Manager</p>
  </div>

  <p class="address">42 Harbour Lane,<br>Level 3 Marine Court</p>
</section>

<section class="card card--back" aria-label="Business card back">
  <svg viewBox="0 0 760 434" preserveAspectRatio="none" aria-hidden="true">
    <polygon points="0,0 250,0 250,70 0,70" fill="var(--pink)"/>
    <polygon points="250,0 310,0 310,70 250,70" fill="var(--charcoal)"/>
    <rect x="0" y="150" width="760" height="96" fill="var(--pink)"/>
    <rect x="420" y="246" width="110" height="188" fill="var(--pink)"/>
  </svg>
</section>

</body>
</html>
```